Talvoro Equity LLC

Need Professional Business cards for New Investment Fund

Target Market(s)

High Quality investors

Industry/Entity Type

Financial

Contact Information for Business Card

Phone Number +1 555 284 6190
Name Milan Dorovsky
Title Fund Manager
email md@FundTalvoro.com
Website www.FundTalvoro.com

Colors

Designer to choose colors to be used in the design.

Requirements
Must have
• Must have our Logo and all of the above. Must be made so lettering and loge can be raised

```html
<!DOCTYPE html>
<html lang="en">
<head>
<meta charset="utf-8">
<title>Talvoro Equity LLC – Business Card</title>
<link rel="stylesheet" href="https://fonts.googleapis.com/css2?family=Arimo:wght@400;700&display=swap">
<style>
  :root {
    --page-bg: #2a2b30;
    --brand-green: #9cc33b;
    --card-grey: #c7c7c7;
    --logo-grey: #b4b4b4;
    --mark-faint: #b3b3b3;
    --text-dark: #3a3a3a;
    --text-light: #f4f4f4;
    --icon-white: #ffffff;
  }
  * { box-sizing: border-box; margin: 0; padding: 0; }
  html, body {
    width: 1200px; height: 800px; overflow: hidden;
    background: var(--page-bg);
    font-family: "Arimo", Arial, sans-serif;
  }
  .canvas {
    width: 1200px; height: 800px;
    display: flex; align-items: center; justify-content: center; gap: 50px;
  }
  .card {
    position: relative;
    width: 540px; height: 310px;
    border-radius: 26px;
    overflow: hidden;
  }
  /* Front */
  .card-front {
    background: var(--brand-green);
    display: flex; align-items: center; justify-content: center;
  }
  .front-logo {
    font-size: 40px; font-weight: 700;
    letter-spacing: 6px;
    color: var(--logo-grey);
    text-transform: uppercase;
  }
  /* Back */
  .card-back {
    background: var(--card-grey);
    border: 2px solid var(--brand-green);
  }
  .back-mark {
    position: absolute; left: 30px; bottom: 22px;
    font-size: 36px; font-weight: 700; line-height: 1;
    letter-spacing: 3px;
    color: var(--mark-faint);
    text-transform: uppercase;
  }
  .holder {
    position: absolute; top: 36px; right: 36px; text-align: right;
  }
  .holder-name {
    font-size: 30px; line-height: 1.15; color: var(--text-light); font-weight: 400;
  }
  .holder-title {
    font-size: 16px; color: var(--text-light); margin-top: 4px;
  }
  .contacts {
    position: absolute; top: 118px; right: 36px;
    list-style: none;
    display: flex; flex-direction: column; gap: 10px;
  }
  .contact-item {
    display: flex; align-items: center; gap: 12px;
    font-size: 19px; line-height: 30px; color: var(--text-dark);
  }
  .contact-icon {
    width: 30px; height: 30px; border-radius: 50%;
    background: var(--brand-green);
    display: flex; align-items: center; justify-content: center;
    flex-shrink: 0;
  }
  .contact-icon svg { width: 18px; height: 18px; }
</style>
</head>
<body>
<main class="canvas">
  <section class="card card-front" aria-label="Card front">
    <div class="front-logo">Talvoro</div>
  </section>

  <section class="card card-back" aria-label="Card back">
    <div class="back-mark">Talvoro</div>
    <div class="holder">
      <p class="holder-name">Milan Dorovsky</p>
      <p class="holder-title">Fund Manager</p>
    </div>
    <ul class="contacts">
      <li class="contact-item">
        <span class="contact-icon">
          <svg viewBox="0 0 20 20" fill="none" stroke="var(--icon-white)" stroke-width="1.6">
            <circle cx="10" cy="10" r="8"/>
            <ellipse cx="10" cy="10" rx="3.5" ry="8"/>
            <line x1="2" y1="10" x2="18" y2="10"/>
          </svg>
        </span>
        www.FundTalvoro.com
      </li>
      <li class="contact-item">
        <span class="contact-icon">
          <svg viewBox="0 0 20 20" fill="none" stroke="var(--icon-white)" stroke-width="1.6">
            <rect x="2" y="4.5" width="16" height="11" rx="1"/>
            <polyline points="2,5 10,11 18,5"/>
          </svg>
        </span>
        md@FundTalvoro.com
      </li>
      <li class="contact-item">
        <span class="contact-icon">
          <svg viewBox="0 0 20 20" fill="var(--icon-white)">
            <path d="M5 2.5c.6-.4 1.4-.3 1.8.3l1.6 2.6c.3.6.2 1.3-.3 1.7l-1.2.9c.8 1.8 2.3 3.3 4.1 4.1l.9-1.2c.4-.5 1.1-.6 1.7-.3l2.6 1.6c.6.4.7 1.2.3 1.8l-1 1.5c-.6.8-1.6 1.2-2.6 1C8 15.5 4.5 12 3.5 7.1c-.2-1 .2-2 1-2.6z"/>
          </svg>
        </span>
        +1 555 284 6190
      </li>
    </ul>
  </section>
</main>
</body>
</html>
```